New Digital Marketing Company Needs Web Design

Introduction

Brightcrest gives advice to small businesses about their websites and digital marketing strategies and builds working relationships with clients to understand their business and maximise its online presence.

Brightcrest offers services to support its clients needs such as: website auditing & search engine optimisation (SEO), Quorvo Promoline, Chatterlane advertising, newsletter development & management, online performance reporting, email setup & management, website hosting, maintenance & backup, web development, web updates & web design.

Design Specification

The site should have a clean & professional look and use the colour scheme from the logo (attached below).

The design should consist of 2 templates; The homepage & content page.

Homepage Design

The homepage should have a header with logo, contact number and email and menu. Followed underneath by a slider and then individual blocks for key services. Under the key services should be a testimonial block with 3 testimonials. Finally the footer with company details, menu links and location map.

Header Info:

Contact number: 01632 960481
Email: info@brightcrest-demo.co.uk

Menu: Home Services About Contact

Slider Design:

The slider should be full page and show an image with text.

Key Services:

The key services should have a relevant icon and brief description.

The key services are:

Digital Marketing

Website Hosting & Management

Website Health Check (SEO)

Website Updating & Development

Newsletter Management

Email Management

Note: Lorem Ipsum can be used for brief description...

Testimonials:

There should be 3 testimonials side by side and they should include a headshot image of the person giving the testimonial.

Note: Lorem Ipsum and sample images can be used for testimonials...

Footer:

The footer should have 3 sections:

Menu links:

Digital Marketing About
Quorvo Promoline Contact
Chatterlane Advertising Privacy Policy
Search Engine Optimisation (SEO) Terms & Conditions
Website Hosting FAQ
Newsletter Management

Company Information:

BrightCrest
14 Marlow Close
Thornbury Vale
Wexhamshire
ZZ9 4QT
Tel: 01632 960481

Chatterlane icon - Pipwave icon - Careernest icon

Location

Quorvo map

Footer Bottom:

Copyright message.

Content Design

The content design should have the common header and footer.

Each content page should have a banner for image with text description (page title).

The content page should have area for text description and area for a video display if available.

There should be a right column (possibly) for modules (latest blog, latest Chatterlane feeds, testimonial)

Project Deadline Extended
Reason: I have had to extend the deadline as could not review while on vacation and need to feedback to some designers for content page design. Many thanks for your understanding.

Target Market(s)

Industry/Entity Type

Digital

Number of Pages Required

2 page

Requirements
Must have
• The site should have a clean & professional look and use the colour scheme from the logo (attached below).
• The design should consist of 2 templates; The homepage & content page.

```html
<!DOCTYPE html>
<html lang="en">
<head>
<meta charset="utf-8">
<title>Brightcrest — Digital Solutions</title>
<link rel="stylesheet" href="https://fonts.googleapis.com/css2?family=Lato:wght@300;400;700;900&display=swap">
<style>
:root{
  --plum:#6b1650;
  --plum-deep:#681447;
  --indigo:#453d63;
  --ink:#3d3558;
  --text:#4a4a4a;
  --line:#8e8e96;
  --divider:#5a5277;
  --white:#ffffff;
}
*{margin:0;padding:0;box-sizing:border-box}
html,body{width:856px;height:1200px;overflow:hidden;background:var(--white)}
body{position:relative;font-family:'Lato',sans-serif;color:var(--text)}

.site-header{position:absolute;left:0;top:0;width:856px;height:34px;background:var(--white);border-bottom:1.5px solid var(--plum)}
.brand{position:absolute;left:160px;top:9px;display:flex;align-items:center;gap:4px;font-size:12px;font-weight:700;color:var(--ink)}
.brand-dot{width:10px;height:10px;border-radius:50%;background:var(--plum)}
.header-contact{position:absolute;left:255px;top:4px;font-size:6.4px;font-weight:300;color:var(--ink);line-height:13px}
.header-contact span{display:inline-block;width:9px;color:var(--plum)}
.main-nav{position:absolute;top:12px;left:537px;font-size:7.2px}
.main-nav a{color:var(--plum);text-decoration:none;position:absolute;white-space:nowrap}
.main-nav .active{border-bottom:1px solid var(--plum);padding-bottom:3px}

.hero{position:absolute;left:0;top:34px;width:856px;height:305px;overflow:hidden}
.hero-bg{position:absolute;inset:0;background:linear-gradient(100deg,#3c3556 0%,#453c61 45%,#4a4068 100%)}
.hero-title{position:absolute;left:197px;top:84px;font-size:27px;font-weight:900;color:var(--white);letter-spacing:-0.3px}
.hero-text{position:absolute;left:198px;top:145px;width:442px;font-size:9.4px;line-height:16.5px;color:var(--white)}

.services-title{position:absolute;left:0;top:380px;width:856px;text-align:center;font-size:16px;font-weight:700;color:var(--ink)}
.service-card{position:absolute;width:165px;height:134px;border:1px solid var(--line);display:flex;flex-direction:column;align-items:center;text-align:center;color:var(--ink)}
.service-card svg{margin-top:29px;height:28px}
.service-card p{margin-top:18px;font-size:9.4px;line-height:16.5px}
.service-card.featured{background:var(--plum);border-color:var(--plum);color:var(--white)}
.featured h3{margin-top:12px;font-size:10px;font-weight:400}
.featured p{margin-top:12px;padding:0 14px;font-size:5.6px;font-weight:300;line-height:15.2px}

.testimonials{position:absolute;left:0;top:754px;width:856px;height:266px;background:var(--indigo)}
.testimonials h2{position:absolute;top:42px;width:856px;text-align:center;font-size:16px;font-weight:700;color:var(--white)}
.testimonial{position:absolute;top:84px;width:285px;height:182px;text-align:center;color:var(--white)}
.testimonial+.testimonial{border-left:1px solid var(--divider)}
.avatar{width:58px;height:58px;border-radius:50%;margin:0 auto;border:1px solid var(--white)}
.testimonial h4{margin-top:13px;font-size:7px;font-weight:900}
.testimonial p{margin:6px auto 0;width:192px;font-size:6.4px;font-weight:300;line-height:16.4px}

.site-footer{position:absolute;left:0;top:1020px;width:856px;height:180px;background:var(--plum-deep);color:var(--white)}
.site-footer h5{position:absolute;top:16px;font-size:8.6px;font-weight:700}
.link-col{position:absolute;top:37px;list-style:none;font-size:6.4px;font-weight:300;line-height:16.5px}
.map{position:absolute;left:377px;top:38px;width:133px;height:90px;background:linear-gradient(135deg,#e6e6e4,#d9dad6)}
.address{position:absolute;left:524px;top:37px;font-size:6.4px;font-weight:300;line-height:12px}
.tel{position:absolute;left:524px;top:121px;font-size:6.4px;font-weight:300}
.social{position:absolute;left:600px;top:39px;list-style:none;font-size:6.4px;font-weight:300}
.social li{display:flex;align-items:center;gap:9px;height:13px;margin-bottom:12px}
.social i{display:block;width:13px;height:13px;background:var(--white);border-radius:2px}
.copyright{position:absolute;top:160px;width:856px;text-align:center;font-size:4.8px;font-weight:300}
</style>
</head>
<body>

<header class="site-header">
  <div class="brand"><div class="brand-dot"></div>BrightCrest</div>
  <div class="header-contact">
    <div><span>&#9742;</span>01632 960481</div>
    <div><span>&#9993;</span>info@brightcrest-demo.co.uk</div>
  </div>
  <nav class="main-nav">
    <a class="active" style="left:0">Home</a>
    <a style="left:42px">Services</a>
    <a style="left:91px">About</a>
    <a style="left:133px">Contact</a>
  </nav>
</header>

<section class="hero">
  <div class="hero-bg" role="img" aria-label="Dimmed photo of code on a screen"></div>
  <h1 class="hero-title">DIGITAL SOLUTIONS</h1>
  <p class="hero-text">Brightcrest gives advice to small businesses about their websites and digital marketing strategies and builds working relationships with clients to understand their business and maximise its online presence.</p>
</section>

<h2 class="services-title">Services</h2>

<div class="service-card" style="left:167px;top:428px">
  <svg viewBox="0 0 32 26" width="32"><path d="M1 0v25h31v-2H3V0z" fill="#6b1650"/><path d="M4 22V7l5 6 5-8 6 9 3-3 6 11z" fill="#6b1650"/></svg>
  <p>Digital Marketing</p>
</div>
<div class="service-card" style="left:345px;top:428px">
  <svg viewBox="0 0 24 28" width="24"><ellipse cx="12" cy="4" rx="12" ry="4" fill="#6b1650"/><path d="M0 7c0 2 5 4 12 4s12-2 12-4v5c0 2-5 4-12 4S0 14 0 12zM0 15c0 2 5 4 12 4s12-2 12-4v5c0 2-5 4-12 4S0 22 0 20zM0 23c0 2 5 4 12 4s12-2 12-4v1c0 2-5 4-12 4S0 26 0 24z" fill="#6b1650"/></svg>
  <p>Website Hosting<br>&amp; Management</p>
</div>
<div class="service-card" style="left:524px;top:428px">
  <svg viewBox="0 0 28 28" width="28"><circle cx="11" cy="11" r="8.5" fill="none" stroke="#6b1650" stroke-width="3.5"/><path d="M17 17l9 9" stroke="#6b1650" stroke-width="4.5" stroke-linecap="round"/></svg>
  <p>Website Health<br>Check (SEO)</p>
</div>
<div class="service-card" style="left:167px;top:575px">
  <svg viewBox="0 0 30 22" width="30"><path d="M9 3L2 11l7 8M21 3l7 8-7 8M18 1l-6 20" fill="none" stroke="#6b1650" stroke-width="2.2"/></svg>
  <p>Website Updating<br>&amp; Development</p>
</div>
<div class="service-card" style="left:345px;top:575px">
  <svg viewBox="0 0 32 24" width="32"><rect x="3" y="1" width="28" height="22" fill="none" stroke="#6b1650" stroke-width="2"/><path d="M3 5H1v18h2" fill="none" stroke="#6b1650" stroke-width="2"/><rect x="7" y="5" width="9" height="7" fill="#6b1650"/><path d="M19 6h8M19 10h8M7 15h20M7 19h20" stroke="#6b1650" stroke-width="2"/></svg>
  <p>Newsletter Management</p>
</div>
<div class="service-card featured" style="left:524px;top:575px">
  <h3>Email Management</h3>
  <p>Lorem ipsum dolor sit amet, consectetur adipisicing elit, sed do eiusmod tempor incididunt ut labore et dolore magna aliqua. Ut enim ad minim veniam, quis nostrud exercitation ullamco laboris nisi ut aliquip ex ea commodo consequat.</p>
</div>

<section class="testimonials">
  <h2>Testimonials</h2>
  <div class="testimonial" style="left:0">
    <div class="avatar" role="img" aria-label="Headshot of client" style="background:radial-gradient(circle at 50% 40%,#8a6a58,#2a2224)"></div>
    <h4>-MARCUS DELLOW - CLIENT</h4>
    <p>Lorem ipsum dolor sit amet, consectetur adipisicing elit, sed do eiusmod tempor incididunt ut labore et dolore magna aliqua. Ut enim ad minim veniam, quis nostrud exercitation ullamco laboris nisi ut aliquip ex ea commodo consequat.</p>
  </div>
  <div class="testimonial" style="left:285px">
    <div class="avatar" role="img" aria-label="Headshot of company CEO" style="background:radial-gradient(circle at 50% 40%,#e8cdb0,#9fb0c8)"></div>
    <h4>-LENA ORWICK - CEO COMPANY</h4>
    <p>Lorem ipsum dolor sit amet, consectetur adipisicing elit, sed do eiusmod tempor incididunt ut labore et dolore magna aliqua. Ut enim ad minim veniam, quis nostrud exercitation ullamco laboris nisi ut aliquip ex ea commodo consequat.</p>
  </div>
  <div class="testimonial" style="left:570px">
    <div class="avatar" role="img" aria-label="Headshot of manager" style="background:radial-gradient(circle at 50% 40%,#b98a6c,#5a3a2c)"></div>
    <h4>-TOMAS REYLE - MANAGER</h4>
    <p>Lorem ipsum dolor sit amet, consectetur adipisicing elit, sed do eiusmod tempor incididunt ut labore et dolore magna aliqua. Ut enim ad minim veniam, quis nostrud exercitation ullamco laboris nisi ut aliquip ex ea commodo consequat.</p>
  </div>
</section>

<footer class="site-footer">
  <h5 style="left:160px">Useful Links</h5>
  <ul class="link-col" style="left:160px">
    <li>Digital Marketing</li><li>Quorvo Promoline</li><li>Chatterlane Advertising</li>
    <li>Search Engine Optimisation (SEO)</li><li>Website Hosting</li><li>Newsletter Management</li>
  </ul>
  <ul class="link-col" style="left:288px">
    <li>About</li><li>Contact</li><li>Privacy Policy</li><li>Terms &amp; Conditions</li><li>FAQ</li>
  </ul>
  <h5 style="left:376px">Contact</h5>
  <div class="map" role="img" aria-label="Street map showing the office location"></div>
  <div class="address">BrightCrest<br>14 Marlow Close<br>Thornbury Vale<br>Wexhamshire<br>ZZ9 4QT</div>
  <div class="tel">Tel: 01632 960481</div>
  <ul class="social">
    <li><i></i>t/BrightCrest</li>
    <li><i></i>f/BrightCrest</li>
    <li><i></i>In/BrightCrest</li>
  </ul>
  <div class="copyright">© BrightCrest 2016. All Rights Reserved.</div>
</footer>

</body>
</html>
```